Wirenexa

I'm looking to much improve our current website wirenexa.com
Updates

Low design quality

Target Market(s)

Commercial clients (Not-Residentials)

Industry/Entity Type

Office buildings and Industrial clients

Coding

Coded - Design and coding required

Number of Pages Required

5+ page

Requirements
Must have
• Very professional structured low voltage cabling projects for Wi-Fi, Audio/Video conference rooms, Access Control systems, CCTV.

```html
<!DOCTYPE html>
<html lang="en">
<head>
<meta charset="utf-8">
<title>Wirenexa — Commercial Low-Voltage Cabling</title>
<link rel="stylesheet" href="https://fonts.googleapis.com/css2?family=Manrope:wght@400;500;600;700&family=JetBrains+Mono:wght@400;500;700&display=swap">
<style>
:root{
  --red:#d42027;
  --red-soft:#fdecec;
  --ink:#15171a;
  --text:#3d4148;
  --muted:#7b8089;
  --line:#e4e6ea;
  --bg-grey:#f3f4f6;
  --green:#2f8a4a;
  --green-bg:#eaf6ee;
  --blue:#2a6fb0;
  --blue-bg:#eaf2fb;
  --orange:#c9641a;
  --orange-bg:#fdf1e6;
  --slate-bg:#f1f2f4;
}
*{box-sizing:border-box;margin:0;padding:0}
html,body{width:1200px;height:3160px;overflow:hidden;background:#fff}
body{font-family:"Manrope",sans-serif;color:var(--ink);position:relative}
.mono{font-family:"JetBrains Mono",monospace}
.wrap{width:950px;margin:0 auto;position:relative}
svg{display:block}

/* nav */
.nav{height:49px;border-bottom:1px solid var(--line);display:flex;align-items:center}
.nav .wrap{display:flex;align-items:center}
.brand{display:flex;align-items:center;gap:7px;font-weight:700;font-size:20px;color:var(--red)}
.brand i{width:15px;height:15px;background:var(--red);display:block}
.nav-links{display:flex;gap:20px;margin-left:172px;font-size:11.5px;color:var(--muted)}
.nav-phone{margin-left:auto;font-size:11.5px;color:var(--text);display:flex;gap:5px;align-items:center}
.btn-red{background:var(--red);color:#fff;border-radius:20px;font-weight:700;display:inline-flex;align-items:center;gap:7px}
.nav .btn-red{margin-left:32px;font-size:11.5px;padding:7px 15px}

/* hero */
.hero{height:450px;position:relative}
.hero-left{position:absolute;left:0;top:67px;width:400px}
.badge{display:inline-flex;align-items:center;gap:5px;font-size:9px;color:var(--green);background:var(--green-bg);border:1px solid #cfe8d7;border-radius:20px;padding:3px 9px}
.badge i{width:4px;height:4px;border-radius:50%;background:var(--green)}
.eyebrow{font-size:9px;letter-spacing:.08em;color:var(--muted);margin-top:17px}
.hero h1{font-size:40px;line-height:46px;font-weight:600;margin-top:18px;letter-spacing:-.5px}
.hero h1 span{color:var(--red)}
.hero p{font-size:14.5px;line-height:22.5px;color:var(--text);margin-top:20px}
.hero p b{color:var(--ink);font-weight:600}
.hero-btns{display:flex;gap:13px;margin-top:23px;align-items:center}
.hero-btns .btn-red{font-size:13px;padding:10px 21px}
.btn-ghost{border:1px solid var(--line);border-radius:20px;padding:7px 15px;font-size:11.5px;font-weight:600;color:var(--text);display:inline-flex;gap:6px;align-items:center}
.hero-img{position:absolute;left:455px;top:39px;width:495px;height:241px;border-radius:9px;background:linear-gradient(135deg,#0d1520 0%,#1d3d6b 45%,#2c6fc0 60%,#0e1622 100%)}
.hero-img .cap{position:absolute;right:20px;bottom:18px;font-size:9px;color:#fff}
.callback{position:absolute;left:455px;top:293px;width:495px;height:120px;border:1px solid var(--line);border-radius:9px;padding:24px 18px}
.cb-head{display:flex;gap:10px;align-items:center}
.cb-ico{width:24px;height:24px;border-radius:50%;background:var(--red-soft);display:flex;align-items:center;justify-content:center}
.cb-head b{font-size:11px;display:block}
.cb-head small{font-size:8px;color:var(--muted)}
.cb-row{display:flex;gap:9px;margin-top:12px}
.field{width:159px;height:30px;border:1px solid var(--line);border-radius:5px;font-size:10.5px;color:#a4a8af;padding:8px 10px}
.cb-row .btn-red{font-size:11.5px;padding:7px 15px;margin-left:1px}

/* stats */
.stats{height:79px;border:1px solid var(--line);border-radius:7px;display:flex;align-items:center}
.stat{flex:1;text-align:center;border-right:1px solid var(--line);height:46px;padding-top:4px}
.stat:last-child{border-right:0}
.stat b{font-family:"JetBrains Mono",monospace;font-size:21px;font-weight:500;display:block}
.stat small{font-family:"JetBrains Mono",monospace;font-size:8.5px;color:var(--muted);letter-spacing:.03em}

/* section heads */
.sec-head{text-align:center}
.sec-head .eyebrow{margin-top:0}
.sec-head h2{font-size:29px;line-height:35px;font-weight:600;margin-top:14px;letter-spacing:-.3px}
.sec-head h2 span{color:var(--red)}
.sec-head p{font-size:14.5px;line-height:22px;color:var(--text);margin:18px auto 0;width:440px}

/* services */
.services{padding-top:104px}
.grid{display:grid;grid-template-columns:repeat(4,223px);gap:19px 19px;margin-top:40px}
.card{border:1px solid var(--line);border-radius:7px;padding:20px 19px;display:flex;flex-direction:column}
.row1 .card{height:317px}
.row2{margin-top:19px}
.row2 .card{height:354px}
.ico{width:26px;height:26px;border-radius:5px;display:flex;align-items:center;justify-content:center}
.card h3{font-size:15.5px;font-weight:600;margin-top:16px;line-height:20px}
.card p{font-size:11.5px;line-height:18.3px;color:var(--text);margin-top:10px}
.tags{display:flex;flex-wrap:wrap;gap:5px;margin-top:auto}
.tag{font-family:"JetBrains Mono",monospace;font-size:8.5px;border-radius:3px;padding:3px 7px;border:1px solid}
.t-blue{color:var(--blue);background:var(--blue-bg);border-color:#cfe0f3}
.t-green{color:var(--green);background:var(--green-bg);border-color:#cfe8d7}
.t-orange{color:var(--orange);background:var(--orange-bg);border-color:#f4d9c2}
.t-slate{color:#4a4f57;background:var(--slate-bg);border-color:#dcdfe3}
.quote{font-size:10.5px;color:var(--red);font-weight:600;margin-top:18px}

/* projects */
.projects{background:var(--bg-grey);height:638px;margin-top:75px;padding-top:79px}
.proj-grid{display:grid;grid-template-columns:repeat(3,304px);gap:19px;margin-top:38px}
.proj{background:#fff;border:1px solid var(--line);border-radius:7px;overflow:hidden;height:233px}
.proj-img{height:172px;position:relative}
.proj-img .lbl{position:absolute;left:9px;top:10px;font-size:9px;color:#fff;font-weight:700;background:rgba(0,0,0,.35);padding:2px 6px;border-radius:3px}
.proj-img .cap{position:absolute;right:9px;bottom:10px;font-size:8.5px;color:#fff;background:rgba(0,0,0,.45);padding:2px 6px;border-radius:3px}
.proj-body{padding:9px 13px}
.proj-body h4{font-size:11px;font-weight:700}
.proj-meta{display:flex;gap:6px;align-items:center;margin-top:7px}
.proj-meta .count{margin-left:auto;font-family:"JetBrains Mono",monospace;font-size:8.5px;color:var(--muted)}
.center-btn{text-align:center;margin-top:39px}
.center-btn span{display:inline-block;background:#fff;border:1px solid var(--line);border-radius:18px;padding:7px 16px;font-size:11.5px;font-weight:700}

/* trust */
.trust{height:61px;display:flex;justify-content:center;align-items:center;gap:13px;font-family:"JetBrains Mono",monospace;font-size:9px;letter-spacing:.04em;border-bottom:1px solid var(--line)}
.trust span{display:flex;gap:6px;align-items:center}
.trust em{width:1px;height:12px;background:var(--line)}

/* estimate */
.estimate{background:var(--bg-grey);height:479px;position:relative}
.est-left{position:absolute;left:0;top:91px;width:360px}
.est-left .eyebrow{margin-top:0}
.est-left h2{font-size:29px;line-height:34px;font-weight:600;margin-top:18px}
.est-left h2 span{color:var(--red)}
.est-left p{font-size:14.5px;line-height:22px;color:var(--text);margin-top:20px}
.checks{margin-top:18px;display:flex;flex-direction:column;gap:13px;font-size:11px;color:var(--text)}
.checks li{list-style:none;display:flex;gap:9px;align-items:center}
.form{position:absolute;left:417px;top:77px;width:500px;height:326px;background:#fff;border:1px solid var(--line);border-radius:9px;padding:24px 25px}
.steps{display:flex;align-items:center}
.step{width:20px;height:20px;border-radius:50%;border:1px solid #c8cbd0;font-size:8.5px;display:flex;align-items:center;justify-content:center;color:var(--muted);background:#f6f7f8}
.step.on{border:1.5px solid var(--red);color:var(--red);background:#fff}
.steps i{flex:1;height:1px;background:var(--line)}
.form .eyebrow{color:var(--red);margin-top:10px}
.form .q{font-size:11.5px;font-weight:600;margin-top:30px}
.opts{display:flex;gap:9px;margin-top:15px}
.opts span{border:1px solid var(--line);border-radius:20px;padding:10px 16px;font-size:11.5px;font-weight:600;color:var(--text);background:#fafbfc}
.form-foot{position:absolute;left:25px;right:25px;bottom:24px;border-top:1px solid var(--line);padding-top:14px;display:flex;justify-content:flex-end}
.form-foot span{background:#f1a3a6;color:#fff;border-radius:16px;font-size:11.5px;font-weight:700;padding:6px 15px}

/* footer */
.footer{height:329px;padding-top:56px}
.foot-cols{display:flex}
.foot-brand{width:275px}
.foot-brand p{font-size:11px;line-height:17px;color:var(--muted);margin-top:18px;width:215px}
.socials{display:flex;gap:15px;margin-top:22px}
.socials i{width:20px;height:20px;border-radius:50%;border:1px solid var(--line);background:#f6f7f8;display:block}
.fcol{width:233px}
.fcol h5{font-family:"JetBrains Mono",monospace;font-size:8.5px;font-weight:500;color:var(--muted);letter-spacing:.08em}
.fcol ul{list-style:none;margin-top:12px}
.fcol li{font-size:11px;color:var(--text);line-height:24.5px}
.fcol.cert li{line-height:22px;display:flex;gap:7px;align-items:center}
.fcol.cert li::before{content:"";width:4px;height:4px;border-radius:50%;background:var(--green)}
.foot-bottom{position:absolute;left:0;right:0;top:260px;border-top:1px solid var(--line);display:flex;justify-content:space-between;padding-top:15px;font-family:"JetBrains Mono",monospace;font-size:8.5px;color:var(--muted)}
.foot-bottom b{color:var(--red);font-weight:400}
</style>
</head>
<body>

<header class="nav">
  <div class="wrap">
    <div class="brand"><i></i>Wirenexa</div>
    <nav class="nav-links"><span>Services</span><span>Projects</span><span>About</span><span>Contact</span></nav>
    <div class="nav-phone">
      <svg width="11" height="11" viewBox="0 0 24 24" fill="none" stroke="currentColor" stroke-width="2"><path d="M22 16.9v3a2 2 0 0 1-2.2 2A19.8 19.8 0 0 1 2 4.2 2 2 0 0 1 4 2h3a2 2 0 0 1 2 1.7c.1 1 .4 1.9.7 2.8a2 2 0 0 1-.5 2.1L8 9.8a16 16 0 0 0 6 6l1.3-1.3a2 2 0 0 1 2.1-.4c.9.3 1.8.6 2.8.7a2 2 0 0 1 1.7 2z"/></svg>
      (703) 555-0187
    </div>
    <span class="btn-red">Get a Free Estimate <svg width="10" height="10" viewBox="0 0 24 24" fill="none" stroke="#fff" stroke-width="2.5"><path d="M5 12h14M13 6l6 6-6 6"/></svg></span>
  </div>
</header>

<section class="hero wrap">
  <div class="hero-left">
    <span class="badge mono"><i></i>VERITEST VX-8000 CERTIFIED</span>
    <div class="eyebrow mono">COMMERCIAL LOW-VOLTAGE SPECIALISTS</div>
    <h1>Professional Cabling<br><span>for Your Business</span></h1>
    <p>Certified structured cabling, fiber optic, video surveillance, access control, WAP, Skyreach, and conference room AV for <b>offices and warehouses</b> across Virginia, DC, and Maryland.</p>
    <div class="hero-btns">
      <span class="btn-red">Get a Free Estimate <svg width="11" height="11" viewBox="0 0 24 24" fill="none" stroke="#fff" stroke-width="2.5"><path d="M5 12h14M13 6l6 6-6 6"/></svg></span>
      <span class="btn-ghost"><svg width="11" height="11" viewBox="0 0 24 24" fill="none" stroke="currentColor" stroke-width="2"><path d="M3 7v12h18V9h-9l-2-2z"/></svg>View Projects</span>
    </div>
  </div>
  <div class="hero-img" role="img" aria-label="Network rack with neatly routed blue patch cables"><span class="cap mono">CAT6A / Veritest VX-8000</span></div>
  <div class="callback">
    <div class="cb-head">
      <span class="cb-ico"><svg width="12" height="12" viewBox="0 0 24 24" fill="none" stroke="#d42027" stroke-width="2"><path d="M22 16.9v3a2 2 0 0 1-2.2 2A19.8 19.8 0 0 1 2 4.2 2 2 0 0 1 4 2h3a2 2 0 0 1 2 1.7c.1 1 .4 1.9.7 2.8a2 2 0 0 1-.5 2.1L8 9.8a16 16 0 0 0 6 6l1.3-1.3a2 2 0 0 1 2.1-.4c.9.3 1.8.6 2.8.7a2 2 0 0 1 1.7 2z"/></svg></span>
      <div><b>Request a Callback</b><small>We call you — not the other way around.</small></div>
    </div>
    <div class="cb-row">
      <div class="field">Your name</div>
      <div class="field">Business phone *</div>
      <span class="btn-red">Request Call <svg width="10" height="10" viewBox="0 0 24 24" fill="none" stroke="#fff" stroke-width="2.5"><path d="M5 12h14M13 6l6 6-6 6"/></svg></span>
    </div>
  </div>
</section>

<div class="wrap stats">
  <div class="stat"><b style="color:var(--red)">30yr</b><small>System Warranty</small></div>
  <div class="stat"><b style="color:var(--green)">100%</b><small>Veritest VX-8000 Pass Rate</small></div>
  <div class="stat"><b style="color:var(--blue)">10Gbps</b><small>Network Backbone</small></div>
  <div class="stat"><b style="color:var(--orange)">150+</b><small>Commercial Projects</small></div>
</div>

<section class="services wrap">
  <div class="sec-head">
    <div class="eyebrow mono">WHAT WE DO</div>
    <h2>Full-Spectrum Low-Voltage<br><span>for Commercial Spaces</span></h2>
    <p>From copper and fiber backbones to surveillance, wireless, and conference room AV — we handle the complete low-voltage scope for offices and warehouses.</p>
  </div>
  <div class="grid row1">
    <article class="card">
      <div class="ico" style="background:var(--blue-bg)"><svg width="13" height="13" viewBox="0 0 24 24" fill="none" stroke="#2a6fb0" stroke-width="2"><path d="M6 3v8a4 4 0 0 0 8 0V7a3 3 0 0 1 6 0v14"/></svg></div>
      <h3>Structured Cabling</h3>
      <p>Certified copper CAT6/CAT6A and fiber optic backbone installations for offices, warehouses, and multi-floor commercial buildings. Every run Veritest-tested and documented.</p>
      <div class="tags"><span class="tag t-blue">CAT6A</span><span class="tag t-slate">OM4 Fiber</span><span class="tag t-green">Veritest Certified</span></div>
      <div class="quote">Request a Quote →</div>
    </article>
    <article class="card">
      <div class="ico" style="background:var(--blue-bg)"><svg width="13" height="13" viewBox="0 0 24 24" fill="none" stroke="#2a6fb0" stroke-width="2"><rect x="3" y="6" width="18" height="13" rx="2"/><circle cx="12" cy="12.5" r="3.5"/></svg></div>
      <h3>Video Surveillance</h3>
      <p>End-to-end IP camera systems with PoE switch wiring and central NVR storage. Scalable from a single-floor office to multi-site commercial deployments.</p>
      <div class="tags"><span class="tag t-blue">IP / PoE</span><span class="tag t-slate">4K Cameras</span><span class="tag t-slate">NVR Storage</span></div>
      <div class="quote">Request a Quote →</div>
    </article>
    <article class="card">
      <div class="ico" style="background:var(--green-bg)"><svg width="13" height="13" viewBox="0 0 24 24" fill="none" stroke="#2f8a4a" stroke-width="2"><path d="M12 3l8 3v6c0 5-3.5 8-8 9-4.5-1-8-4-8-9V6z"/><path d="M9 12l2 2 4-4"/></svg></div>
      <h3>Access Control</h3>
      <p>Door-strike wiring, card reader installations, and controller panel enclosures for commercial properties. Secure entry points with clean, concealed cabling.</p>
      <div class="tags"><span class="tag t-green">Door Strike</span><span class="tag t-green">Card Reader</span><span class="tag t-blue">CAT6A</span></div>
      <div class="quote">Request a Quote →</div>
    </article>
    <article class="card">
      <div class="ico" style="background:var(--orange-bg)"><svg width="13" height="13" viewBox="0 0 24 24" fill="none" stroke="#c9641a" stroke-width="2"><path d="M4 10a12 12 0 0 1 16 0M7 13.5a7 7 0 0 1 10 0M10 17a2.5 2.5 0 0 1 4 0"/></svg></div>
      <h3>Wireless Access Points</h3>
      <p>High-density commercial WAP deployment with site surveys and signal mapping. Coverage-optimized layouts for open offices, warehouses, and multi-floor buildings.</p>
      <div class="tags"><span class="tag t-orange">High-Density</span><span class="tag t-orange">Wi-Fi 6E</span><span class="tag t-slate">Site Survey</span></div>
      <div class="quote">Request a Quote →</div>
    </article>
  </div>
  <div class="grid row2" style="margin-top:19px">
    <article class="card">
      <div class="ico" style="background:var(--blue-bg)"><svg width="13" height="13" viewBox="0 0 24 24" fill="none" stroke="#2a6fb0" stroke-width="2"><rect x="3" y="4" width="18" height="12" rx="2"/><path d="M9 20h6M12 16v4"/></svg></div>
      <h3>Point of Sale (POS)</h3>
      <p>Network infrastructure and cabling for POS systems in retail and commercial environments. Reliable, clean runs from switch to terminal — no downtime, no mess.</p>
      <div class="tags"><span class="tag t-blue">Network Infra</span><span class="tag t-slate">Retail</span></div>
      <div class="quote">Request a Quote →</div>
    </article>
    <article class="card">
      <div class="ico" style="background:var(--orange-bg)"><svg width="13" height="13" viewBox="0 0 24 24" fill="none" stroke="#c9641a" stroke-width="2"><path d="M5 19a9 9 0 0 1 0-12l12 12a9 9 0 0 1-12 0z"/><path d="M14 6a4 4 0 0 1 4 4M14 2a8 8 0 0 1 8 8"/></svg></div>
      <h3>Skyreach</h3>
      <p>Commercial Skyreach dish installation and full LAN integration. We handle the roof mount, cable routing, and network handoff so your team is online from day one.</p>
      <div class="tags"><span class="tag t-orange">Commercial Install</span><span class="tag t-blue">LAN Integration</span></div>
      <div class="quote">Request a Quote →</div>
    </article>
    <article class="card">
      <div class="ico" style="background:var(--blue-bg)"><svg width="13" height="13" viewBox="0 0 24 24" fill="none" stroke="#2a6fb0" stroke-width="2"><rect x="3" y="4" width="18" height="12" rx="2"/><path d="M9 20h6M12 16v4"/></svg></div>
      <h3>Conference Room Technology</h3>
      <p>Full AV integration for boardrooms and meeting spaces. Zero-visible-cable setups with ceiling-mount displays, PTZ cameras, HDMI plates, and structured conduit routing.</p>
      <div class="tags"><span class="tag t-blue">AV Integration</span><span class="tag t-slate">Zero-Cable</span><span class="tag t-blue">PTZ Camera</span></div>
      <div class="quote">Request a Quote →</div>
    </article>
  </div>
</section>

<section class="projects">
  <div class="wrap">
    <div class="sec-head">
      <div class="eyebrow mono">COMPLETED PROJECTS</div>
      <h2>Built for Offices.<br><span>Certified for Business.</span></h2>
      <p style="width:420px">Every installation is Veritest VX-8000 certified and delivered to NCS-568 standards. Real work, documented results.</p>
    </div>
    <div class="proj-grid">
      <article class="proj">
        <div class="proj-img" role="img" aria-label="Server rack with blue CAT6A cabling" style="background:linear-gradient(135deg,#0c141f,#1f4a85 55%,#0e1724)"><span class="lbl mono">Corporate Office</span><span class="cap mono">CAT6A / Veritest VX-8000</span></div>
        <div class="proj-body"><h4>Multi-Floor CAT6A Backbone</h4><div class="proj-meta"><span class="tag t-blue">CAT6A Copper</span><span class="tag t-green">Veritest Certified</span><span class="count">240 drops</span></div></div>
      </article>
      <article class="proj">
        <div class="proj-img" role="img" aria-label="Executive conference room with long table and wall display" style="background:linear-gradient(160deg,#d9dcdf,#9a9ea3 50%,#5e4a3c)"><span class="lbl mono">Corporate HQ</span><span class="cap mono">HDMI 2.1 / PTZ Camera</span></div>
        <div class="proj-body"><h4>Executive AV Conference Suite</h4><div class="proj-meta"><span class="tag t-blue">Fiber + HDMI</span><span class="tag t-green">Clean Install</span><span class="count">6 AV points</span></div></div>
      </article>
      <article class="proj">
        <div class="proj-img" role="img" aria-label="Building lobby door with card reader panel" style="background:linear-gradient(120deg,#8a7a68,#4c4a47 50%,#9d9b97)"><span class="lbl mono">Commercial Building</span><span class="cap mono">Keycard + Door Strike</span></div>
        <div class="proj-body"><h4>Multi-Door Access Control</h4><div class="proj-meta"><span class="tag t-blue">CAT6 / 22 AWG</span><span class="tag t-green">NCS Compliant</span><span class="count">12 doors</span></div></div>
      </article>
    </div>
    <div class="center-btn"><span>Start Your Project</span></div>
  </div>
</section>

<div class="trust">
  <span><svg width="12" height="12" viewBox="0 0 24 24" fill="none" stroke="#2f8a4a" stroke-width="2"><circle cx="12" cy="12" r="9"/><path d="M8 12l3 3 5-5"/></svg>VERITEST VX-8000 CERTIFIED</span><em></em>
  <span><svg width="12" height="12" viewBox="0 0 24 24" fill="none" stroke="#2a6fb0" stroke-width="2"><circle cx="12" cy="8" r="5"/><path d="M9 13l-1 8 4-2 4 2-1-8"/></svg>CABLEPRO GUILD MEMBER</span><em></em>
  <span><svg width="12" height="12" viewBox="0 0 24 24" fill="none" stroke="#d42027" stroke-width="2"><path d="M12 3l9 5-9 5-9-5zM3 13l9 5 9-5"/></svg>NCS-568 COMPLIANT</span><em></em>
  <span><svg width="12" height="12" viewBox="0 0 24 24" fill="none" stroke="#c9641a" stroke-width="2"><circle cx="9" cy="8" r="4"/><path d="M2 21a7 7 0 0 1 14 0M17 11l2 2 4-4"/></svg>30-YEAR SYSTEM WARRANTY</span>
</div>

<section class="estimate">
  <div class="wrap" style="height:100%">
    <div class="est-left">
      <div class="eyebrow mono">GET STARTED</div>
      <h2>Request Your<br><span>Free Estimate</span></h2>
      <p>Tell us about your project and we'll put together a detailed estimate for your commercial space — no pressure, no obligation.</p>
      <ul class="checks">
        <li><svg width="11" height="11" viewBox="0 0 24 24" fill="none" stroke="#2f8a4a" stroke-width="2.5"><circle cx="12" cy="12" r="10"/><path d="M8 12l3 3 5-5"/></svg>Respond within 1 business day</li>
        <li><svg width="11" height="11" viewBox="0 0 24 24" fill="none" stroke="#2f8a4a" stroke-width="2.5"><circle cx="12" cy="12" r="10"/><path d="M8 12l3 3 5-5"/></svg>Veritest-certified installations</li>
        <li><svg width="11" height="11" viewBox="0 0 24 24" fill="none" stroke="#2f8a4a" stroke-width="2.5"><circle cx="12" cy="12" r="10"/><path d="M8 12l3 3 5-5"/></svg>Commercial clients only</li>
      </ul>
    </div>
    <div class="form">
      <div class="steps"><span class="step on mono">1</span><i></i><span class="step mono">2</span><i></i><span class="step mono">3</span><i></i><span class="step mono">4</span></div>
      <div class="eyebrow mono">PROJECT TYPE</div>
      <div class="q">What type of project is this?</div>
      <div class="opts"><span>New Construction</span><span>Retrofit / Upgrade</span><span>Expansion</span></div>
      <div class="form-foot"><span>Next →</span></div>
    </div>
  </div>
</section>

<footer class="footer">
  <div class="wrap" style="height:100%">
    <div class="foot-cols">
      <div class="foot-brand">
        <div class="brand"><i></i>Wirenexa</div>
        <p>Commercial low-voltage cabling specialists serving offices and warehouses across Virginia, Washington DC, and Maryland.</p>
        <div class="socials"><i></i><i></i><i></i><i></i><i></i></div>
      </div>
      <div class="fcol"><h5>SERVICES</h5><ul><li>Structured Cabling (Copper &amp; Fiber)</li><li>Video Surveillance / CCTV</li><li>Access Control</li><li>Wireless Access Points (WAP)</li><li>Point of Sale (POS)</li><li>Skyreach</li><li>Conference Room Technology</li></ul></div>
      <div class="fcol"><h5>COMPANY</h5><ul><li>About</li><li>Portfolio</li><li>Services</li><li>Get an Estimate</li></ul></div>
      <div class="fcol cert"><h5>CERTIFICATIONS</h5><ul><li>Veritest VX-8000 Certified</li><li>CablePro Guild Member</li><li>NCS-568 Compliant</li><li>30-Year System Warranty</li></ul></div>
    </div>
    <div class="foot-bottom"><span>© 2026 Wirenexa. All rights reserved.</span><b>wirenexa.com</b></div>
  </div>
</footer>

</body>
</html>
```